Hack my website! Tall Harbor needs a site

We hack stuff. No joke, that is what we do, but we are the good guys!

We do security consulting, specifically offensive security. The technical term is "Penetration Testing", but you probably know it as "hacking". Companies hire us to break in before the bad guys do. (I have a very cool job :) ).

I need a web site to describe our offerings and connect with clients.

I've included my business card and logo so you can understand what I'm looking for on the website and the color scheme.

Tag line:
Offensive Services from Offensive Minds

Target Market(s)

Medium to large businesses

Industry/Entity Type

Computer Security

Coding

Coded - Design and coding required

Number of Pages Required

2 page

Font styles to use
Sans Serif

Colors

Designer to choose colors to be used in the design.

Requirements
Must have
• Flat, clean, professional look
Nice to have
• Bonus for bootstrap. See the uploaded logo for the current colors. I'd really like this to look decent on a phone too.
Should not have
• 1. Black background
• 2. The business card is to show the colors and theme so far. Please, do NOT just slam that into the middle of the site since it doesn't make sense. It feels odd that I have to say that, but I've received multiple submissions where people have done this.

```html
<!DOCTYPE html>
<html lang="en">
<head>
<meta charset="utf-8">
<title>Tall Harbor — Offensive Security</title>
<link href="https://fonts.googleapis.com/css2?family=Open+Sans:wght@400;600;700;800&display=swap" rel="stylesheet">
<style>
:root{
  --red:#d0202a;
  --red-dark:#b3161f;
  --ink:#333333;
  --text:#555555;
  --topbar:#3a3a3a;
  --footer:#2b2b2b;
  --footer-base:#1f1f1f;
  --grey-bg:#f2f2f2;
  --white:#ffffff;
  --line:#d6d6d6;
}
*{box-sizing:border-box;margin:0;padding:0}
html,body{width:1200px;height:3509px;overflow:hidden}
body{font-family:"Open Sans",Arial,sans-serif;color:var(--text);background:var(--white);position:relative}
.abs{position:absolute}

/* top bar */
.topbar{position:absolute;top:0;left:0;width:1200px;height:56px;background:var(--topbar);color:#eee;font-size:15px}
.topbar .contact{position:absolute;right:75px;top:17px;display:flex;gap:30px;align-items:center}
.topbar .contact span{display:flex;align-items:center;gap:10px}

/* nav */
.navbar{position:absolute;top:56px;left:0;width:1200px;height:74px;background:var(--white)}
.brand{position:absolute;left:75px;top:14px;display:flex;flex-direction:column;align-items:center}
.brand .mark{width:26px;height:26px;background:var(--red)}
.brand .name{font-weight:700;font-size:19px;letter-spacing:3px;color:var(--red);margin-top:4px}
.nav{position:absolute;top:31px;left:0;width:1200px;font-size:15px;font-weight:600;color:var(--ink)}
.nav a{position:absolute;text-decoration:none;color:inherit}
.nav a.active{color:var(--red)}

/* hero */
.hero{position:absolute;top:130px;left:0;width:1200px;height:532px;background:linear-gradient(115deg,#2b2f3a 0%,#1e3a5c 45%,#2d6f9c 75%,#1b2b44 100%)}
.hero h1{position:absolute;left:0;width:1200px;top:215px;text-align:center;font-weight:800;font-size:40px;color:#fff;line-height:54px;letter-spacing:.5px}
.hero h1 span{background:rgba(190,40,55,.75);padding:0 10px}
.dots{position:absolute;top:484px;left:566px;display:flex;gap:10px}
.dots i{width:10px;height:10px;border-radius:50%;background:#fff;display:block}
.dots i:first-child{background:var(--red)}

/* section heading */
.sec-head{position:absolute;left:0;width:1200px;text-align:center}
.divider{position:absolute;left:432px;width:336px;height:20px}
.divider::before{content:"";position:absolute;left:0;right:0;top:10px;height:1px;background:var(--line)}
.divider::after{content:"";position:absolute;left:158px;top:0;width:20px;height:20px;background:var(--red)}
.sec-title{position:absolute;left:0;width:1200px;text-align:center;font-size:26px;font-weight:700;color:var(--ink);letter-spacing:.5px}
.sec-title em{font-style:normal;color:var(--red)}
.lead{position:absolute;text-align:center;font-size:15px;line-height:23px;color:var(--text)}
.btn{position:absolute;background:#444;color:#fff;font-size:14px;font-weight:700;text-align:center;line-height:43px;letter-spacing:.5px}

/* services */
.services-bg{position:absolute;top:1018px;left:0;width:1200px;height:643px}
.card{position:absolute;top:1266px;width:330px;height:246px;background:#fff;text-align:center;padding:20px 28px}
.card svg{display:block;margin:0 auto 12px}
.card h3{font-size:17px;font-weight:600;color:var(--red);line-height:22px;margin-bottom:14px}
.card p{font-size:13.5px;line-height:21px;color:var(--text)}
.arrow{position:absolute}

/* testimonials */
.avatar{position:absolute;top:1839px;left:558px;width:84px;height:84px;background:linear-gradient(180deg,#e9e5e0,#c9c3bb)}
.quote{position:absolute;top:1947px;left:170px;width:860px;text-align:center;font-style:italic;font-size:14.5px;line-height:23px;color:var(--text)}
.who{position:absolute;top:2080px;left:0;width:1200px;text-align:center;font-weight:700;font-size:15px;color:var(--red)}

/* clients */
.clients{position:absolute;top:2350px;left:170px;width:860px;display:flex;justify-content:space-between;align-items:center;font-size:19px;font-weight:700;color:#555}

/* blog */
.post{position:absolute;top:2607px;width:330px}
.post .thumb{height:224px}
.post h4{margin-top:30px;font-size:18px;line-height:22px;font-weight:700;color:var(--red)}
.post p{margin-top:14px;font-size:13.5px;line-height:21px;color:var(--text)}

/* footer band */
.signup{position:absolute;top:3084px;left:0;width:1200px;height:84px;background:var(--red);color:#fff;font-weight:700;font-size:13px}
.signup .label{position:absolute;left:75px;top:34px}
.signup .field{position:absolute;left:192px;top:24px;width:242px;height:40px;background:#fff;color:#444;font-weight:400;font-size:13px;padding:11px 12px}
.signup .go{position:absolute;left:392px;top:24px;width:42px;height:40px;background:#222}
.footer-brand{position:absolute;top:3060px;left:530px;width:140px;text-align:center}
.footer-brand .mark{width:44px;height:44px;margin:0 auto;background:var(--red);border:3px solid #fff}
.footer-brand .name{color:#fff;font-size:18px;font-weight:700;letter-spacing:3px;margin-top:8px}
.follow{position:absolute;right:75px;top:31px;display:flex;align-items:center;gap:18px}
.follow i{display:block;width:20px;height:20px;border-radius:50%;background:#fff}

.footer{position:absolute;top:3168px;left:0;width:1200px;height:284px;background:var(--footer);color:#ddd;font-size:13.5px}
.col{position:absolute;top:42px}
.col h5{font-size:14px;font-weight:700;color:#fff;margin-bottom:12px}
.col li{list-style:none;line-height:28px}
.col .row{display:flex;align-items:center;gap:14px;line-height:30px}
.map{position:absolute;top:45px;left:845px;width:283px;height:185px;background:linear-gradient(135deg,#e8ecdf,#cfdccb 60%,#dfe4d4)}
.base{position:absolute;top:3452px;left:0;width:1200px;height:57px;background:var(--footer-base);color:#999;font-size:12px;text-align:center;line-height:57px}
</style>
</head>
<body>

<header class="topbar">
  <div class="contact">
    <span><svg width="14" height="14" viewBox="0 0 24 24"><path fill="#eee" d="M6.6 10.8a15 15 0 0 0 6.6 6.6l2.2-2.2c.3-.3.7-.4 1-.2 1.1.4 2.3.6 3.6.6.6 0 1 .4 1 1V20c0 .6-.4 1-1 1A17 17 0 0 1 3 4c0-.6.4-1 1-1h3.5c.6 0 1 .4 1 1 0 1.3.2 2.5.6 3.6.1.3 0 .7-.2 1z"/></svg>555. 014. 2290</span>
    <span><svg width="15" height="12" viewBox="0 0 24 18"><path fill="#eee" d="M0 0h24v2L12 10 0 2zM0 4l12 8 12-8v14H0z"/></svg>info@tallharbor.example</span>
  </div>
</header>

<nav class="navbar">
  <div class="brand"><div class="mark"></div><div class="name">TALL HARBOR</div></div>
  <div class="nav">
    <a class="active" style="left:435px">HOME</a>
    <a style="left:515px">ABOUT US</a>
    <a style="left:624px">SERVICES</a>
    <a style="left:726px">CLIENTS</a>
    <a style="left:821px">BLOG</a>
    <a style="left:895px">LATEST NEWS</a>
    <a style="left:1030px">CONTACT US</a>
  </div>
</nav>

<section class="hero" role="img" aria-label="Photo of a person touching a glowing penetration test interface with lock icons">
  <h1><span>OFFENSIVE SERVICES FROM</span><br><span>OFFENSIVE MINDS</span></h1>
  <div class="dots"><i></i><i></i><i></i><i></i></div>
</section>

<!-- welcome -->
<div class="divider" style="top:704px"></div>
<h2 class="sec-title" style="top:740px">WELCOME TO <em>TALL HARBOR</em></h2>
<p class="lead" style="top:786px;left:75px;width:1050px">Aliquam molestie, mi et imperdiet euismod, dui purus auctor tellus, et interdum lacus lectus et ante. Sed accumsan sollicitudin sapien, sit amet adipiscing turpis gravida ac. In congue, neque ac lobortis volutpat, libero mauris varius mi, vitae suscipit ipsum ligula vitae risus. Duis aliquam nibh a dui iaculis viverra id a velit. Vivamus egestas risus in magna varius commodo. Sed semper viverra egestas.<br>Etiam pretium porttitor lectus, vel ornare neque porta volutpat.</p>
<div class="btn" style="top:917px;left:510px;width:180px">READ MORE</div>

<!-- services -->
<svg class="services-bg" viewBox="0 0 1200 643" preserveAspectRatio="none"><polygon points="0,0 600,22 1200,0 1200,643 0,643" fill="#f2f2f2"/></svg>
<div class="divider" style="top:1101px"></div>
<h2 class="sec-title" style="top:1138px">OUR <em>SERVICES</em></h2>
<p class="lead" style="top:1186px;left:75px;width:1050px">Red Team Adversary Simulation - A goal based assessment where we attack just like a real world adversary. This includes external attacks and targeted phishing to demonstrate the real risk to your data.</p>

<svg class="arrow" style="left:44px;top:1372px" width="14" height="24" viewBox="0 0 14 24"><path d="M12 2 2 12l10 10" stroke="#888" stroke-width="3" fill="none"/></svg>
<svg class="arrow" style="left:1140px;top:1372px" width="14" height="24" viewBox="0 0 14 24"><path d="m2 2 10 10L2 22" stroke="#888" stroke-width="3" fill="none"/></svg>

<div class="card" style="left:75px">
  <svg width="36" height="46" viewBox="0 0 36 46"><path d="M0 0h24l12 12v34H0z" fill="#666"/><path d="M24 0v12h12" fill="#999"/><rect x="7" y="20" width="22" height="3" fill="#fff"/><rect x="7" y="27" width="22" height="3" fill="#fff"/><rect x="7" y="34" width="22" height="3" fill="#fff"/></svg>
  <h3>Internal Pivot Assessment &amp; Post Exploitation</h3>
  <p>We start as a low privileged users and attempted to move through the network in an attempt to access the data the matters to you.</p>
</div>
<div class="card" style="left:435px">
  <svg width="52" height="46" viewBox="0 0 52 46"><circle cx="18" cy="26" r="13" fill="none" stroke="#666" stroke-width="7" stroke-dasharray="5 3"/><circle cx="40" cy="12" r="8" fill="none" stroke="#666" stroke-width="5" stroke-dasharray="4 2"/></svg>
  <h3>Advanced Product, Hardware &amp; RF Testing</h3>
  <p>This a highly customized assessment designed for you and your hardware. Depending on the product we will analyze custom RF protocols..</p>
</div>
<div class="card" style="left:793px">
  <svg width="28" height="46" viewBox="0 0 28 46"><rect x="1" y="1" width="26" height="44" rx="4" fill="none" stroke="#666" stroke-width="3"/><rect x="5" y="7" width="18" height="28" fill="#666"/><circle cx="14" cy="40" r="2" fill="#666"/></svg>
  <h3>Mobile Application Assessment</h3>
  <p>We look at your mobile application and the associated infrastructure to find configuration weaknesses, server-side issues, insecure..</p>
</div>
<div class="btn" style="top:1563px;left:497px;width:206px">VIEW ALL SERVICES</div>

<!-- testimonials -->
<div class="divider" style="top:1698px"></div>
<h2 class="sec-title" style="top:1741px">CLIENT <em>TESTIMONIALS</em></h2>
<p class="lead" style="top:1789px;left:0;width:1200px">Vestibulum ante ipsum primis in faucibus orci luctus et ultrices posuere cubilia ...</p>
<svg class="arrow" style="left:513px;top:1870px" width="10" height="20" viewBox="0 0 10 20"><path d="M9 1 1 10l8 9" stroke="#999" stroke-width="2" fill="none"/></svg>
<svg class="arrow" style="left:677px;top:1870px" width="10" height="20" viewBox="0 0 10 20"><path d="m1 1 8 9-8 9" stroke="#999" stroke-width="2" fill="none"/></svg>
<div class="avatar" role="img" aria-label="Portrait photo of the client giving the testimonial"></div>
<p class="quote">" Aliquam molestie, mi et imperdiet euismod, dui purus auctor tellus, et interdum lacus lectus et ante. Sed accumsan sollicitudin sapien, sit amet adipiscing turpis gravida ac. In congue, neque ac lobortis volutpat, libero mauris varius mi, vitae suscipit ipsum ligula vitae risus..."</p>
<svg class="abs" style="left:586px;top:2047px" width="28" height="24" viewBox="0 0 28 24"><path d="M0 0h12v12L6 24H1l5-12H0zM16 0h12v12l-6 12h-5l5-12h-6z" fill="#444"/></svg>
<div class="who">-Name Heading</div>

<!-- clients -->
<svg class="abs" style="top:2153px;left:0" width="1200" height="309" viewBox="0 0 1200 309" preserveAspectRatio="none"><polygon points="0,0 600,22 1200,0 1200,309 0,309" fill="#f2f2f2"/></svg>
<div class="divider" style="top:2236px"></div>
<h2 class="sec-title" style="top:2275px">OUR <em>CLIENTS</em></h2>
<div class="clients">
  <span>Fernmoor</span><span>Quillstone</span><span>Brightlane</span><span>Osmera</span><span>Kestrel</span><span>Vantor</span><span>Halvern</span><span>Orvix</span><span>Tellimar</span>
</div>

<!-- blog -->
<div class="divider" style="top:2498px"></div>
<h2 class="sec-title" style="top:2540px">BLOG <em>POSTS</em></h2>
<article class="post" style="left:75px">
  <div class="thumb" role="img" aria-label="Photo of hands typing on a laptop keyboard in red light" style="background:linear-gradient(135deg,#1a2a4a,#3a4f7a 50%,#8a1f2a)"></div>
  <h4>Nam fermentum vestibulum purus id aliquet aliquam..</h4>
  <p>Vestibulum vel metus sit amet turpis bibendum tincidunt vel sit amet quam habitant morbi tristique senectus et netus et malesuada fames ac turpis egestas..</p>
</article>
<article class="post" style="left:435px">
  <div class="thumb" role="img" aria-label="Photo of a businessman pressing a penetration test interface" style="background:linear-gradient(180deg,#1d3555,#2f5d86 60%,#16263e)"></div>
  <h4>Nam fermentum vestibulum purus id aliquet aliquam..</h4>
  <p>Vestibulum vel metus sit amet turpis bibendum tincidunt vel sit amet quam habitant morbi tristique senectus et netus et malesuada fames ac turpis egestas..</p>
</article>
<article class="post" style="left:793px">
  <div class="thumb" role="img" aria-label="Photo of a hooded hacker surrounded by green code" style="background:linear-gradient(135deg,#0f1a12,#2e5a2a 55%,#0c140e)"></div>
  <h4>Nam fermentum vestibulum purus id aliquet aliquam..</h4>
  <p>Vestibulum vel metus sit amet turpis bibendum tincidunt vel sit amet quam habitant morbi tristique senectus et netus et malesuada fames ac turpis egestas..</p>
</article>

<!-- footer -->
<section class="signup">
  <div class="label">EMAIL SIGN UP</div>
  <div class="field">Enter Email</div>
  <div class="go"><svg width="42" height="40" viewBox="0 0 42 40"><path d="M14 20 29 13l-5 16-3-6z" fill="#fff"/></svg></div>
  <div class="follow"><span style="margin-right:6px">FOLLOW US</span><i></i><i></i><i></i><i></i><i></i></div>
</section>
<div class="footer-brand"><div class="mark"></div><div class="name">TALL HARBOR</div></div>

<footer class="footer">
  <div class="col" style="left:75px"><h5>SITE MAP</h5><ul><li>Home</li><li>About Us</li><li>Services</li><li>Clients</li><li>Blog</li><li>Latest News</li><li>Contact Us</li></ul></div>
  <div class="col" style="left:290px"><h5>SERVICES</h5><ul><li>Internal Pivot Assessment &amp; Post Exploitation</li><li>Advanced Product, Hardware &amp; RF Testing</li><li>Mobile Application Assessment</li><li>External Penetration Testing</li><li>Internal Penetration Testing</li><li>Web Application Penetration Testing</li></ul></div>
  <div class="col" style="left:660px"><h5>CONTACT INFO</h5>
    <div style="line-height:22px;margin-bottom:6px">41 Quarry Lane<br>Eastbridge, EB4 2KL</div>
    <div class="row"><svg width="13" height="13" viewBox="0 0 24 24"><path fill="#ddd" d="M6.6 10.8a15 15 0 0 0 6.6 6.6l2.2-2.2c.3-.3.7-.4 1-.2 1.1.4 2.3.6 3.6.6.6 0 1 .4 1 1V20c0 .6-.4 1-1 1A17 17 0 0 1 3 4c0-.6.4-1 1-1h3.5c.6 0 1 .4 1 1 0 1.3.2 2.5.6 3.6.1.3 0 .7-.2 1z"/></svg>555. 014. 2290</div>
    <div class="row"><svg width="13" height="10" viewBox="0 0 24 18"><path fill="#ddd" d="M0 0h24v2L12 10 0 2zM0 4l12 8 12-8v14H0z"/></svg>info@tallharbor.example</div>
    <div class="row"><svg width="11" height="15" viewBox="0 0 16 22"><path fill="#ddd" d="M8 0a8 8 0 0 1 8 8c0 6-8 14-8 14S0 14 0 8a8 8 0 0 1 8-8zm0 5a3 3 0 1 0 0 6 3 3 0 0 0 0-6z"/></svg>Map Location</div>
  </div>
  <div class="map" role="img" aria-label="Street map showing the office location"></div>
</footer>
<div class="base">Copyright © 2017. Company Name. All Right Reserved</div>

</body>
</html>
```